Business Card for Yachting Management Company

Need a business card design for a new yachting project management company. Attached is the logo for the company.
Our clients are large yacht owners and captains.
Design must be in the style of the logo. Modern, elegant.

Example of data to show:
Peter Hollis
Project Manager
(+34) 612 738 104
peter@quorvane.net
Quorvane Management - Meridel Tower, Office 22 - KRB - Palma de Mallorca

The data above will have to be changed (by me) for the different people in the company over the next years.

Will be printed using PrintNova (Lustre Card Series). They provide these guidelines for the size:
"the actual size of the card is 1050 x 600 pixels. However, the full bleed size is 1083 x 633 pixels, and the safe printing area is 1008 x 558 pixels."

```html
<!DOCTYPE html>
<html lang="en">
<head>
<meta charset="utf-8">
<title>Quorvane Management – Business Card</title>
<link href="https://fonts.googleapis.com/css2?family=Montserrat:wght@400;600;700&display=swap" rel="stylesheet">
<style>
  :root {
    --backdrop: #4a4a4a;
    --card: #161616;
    --card-deep: #0d0d0d;
    --brand-blue: #1273c4;
    --text-light: #e8e8e8;
    --text-grey: #9a9a9a;
  }
  * { margin: 0; padding: 0; box-sizing: border-box; }
  html, body {
    width: 1200px; height: 801px; overflow: hidden;
    background: var(--backdrop);
    font-family: "Montserrat", sans-serif;
  }
  .sheet {
    width: 1200px; height: 801px;
    display: flex; align-items: center; justify-content: center; gap: 40px;
  }
  .card {
    position: relative;
    width: 540px; height: 309px;
    background: var(--card);
    border-radius: 14px;
    border: 2px solid var(--brand-blue);
    overflow: hidden;
    box-shadow: 0 12px 30px rgba(0,0,0,0.35);
  }

  /* Front */
  .front__brand {
    position: absolute; top: 34px; right: 40px;
    font-weight: 700; font-size: 38px; letter-spacing: 1px; line-height: 1;
    color: var(--brand-blue); white-space: nowrap;
  }
  .front__details {
    position: absolute; left: 34px; bottom: 30px; right: 34px;
  }
  .front__company {
    font-weight: 600; font-size: 13px; letter-spacing: 5px;
    text-transform: uppercase; color: var(--brand-blue);
    margin-bottom: 14px; white-space: nowrap;
  }
  .person__name {
    font-weight: 700; font-size: 19px; letter-spacing: 0.5px;
    text-transform: uppercase; color: var(--brand-blue);
  }
  .person__role {
    font-size: 12px; color: var(--text-light); margin-top: 2px; margin-bottom: 12px;
  }
  .address { font-size: 10.5px; line-height: 1.45; color: var(--text-light); margin-bottom: 10px; }
  .contact { list-style: none; font-size: 10.5px; color: var(--text-light); line-height: 1.7; }
  .contact li { display: flex; align-items: center; gap: 7px; }
  .contact svg { width: 11px; height: 11px; flex: none; }
  .icon-phone { fill: var(--brand-blue); }
  .icon-mail { fill: none; stroke: var(--brand-blue); stroke-width: 2.4; stroke-linejoin: round; }

  /* Back */
  .back__watermark {
    position: absolute; top: 36px; right: 34px;
    font-weight: 700; font-size: 80px; letter-spacing: -1px; line-height: 1;
    color: var(--card-deep); white-space: nowrap;
    text-shadow: 0 1px 0 #262626;
  }
  .back__name {
    position: absolute; right: 34px; bottom: 40px;
    font-weight: 600; font-size: 17px; letter-spacing: 6px;
    text-transform: uppercase; color: var(--text-grey);
    white-space: nowrap;
  }
</style>
</head>
<body>
<main class="sheet">
  <section class="card card--front" aria-label="Card front">
    <div class="front__brand">Quorvane</div>
    <div class="front__details">
      <div class="front__company">Quorvane Management</div>
      <div class="person__name">Peter Hollis</div>
      <div class="person__role">Project Manager</div>
      <p class="address">Quorvane Management - Meridel Tower,<br>Office 22 - KRB - Palma de Mallorca</p>
      <ul class="contact">
        <li>
          <svg class="icon-phone" viewBox="0 0 24 24" aria-hidden="true"><path d="M6.6 10.8a15.1 15.1 0 0 0 6.6 6.6l2.2-2.2a1 1 0 0 1 1-.25 11.4 11.4 0 0 0 3.6.57 1 1 0 0 1 1 1V20a1 1 0 0 1-1 1A17 17 0 0 1 3 4a1 1 0 0 1 1-1h3.5a1 1 0 0 1 1 1 11.4 11.4 0 0 0 .57 3.6 1 1 0 0 1-.25 1z"/></svg>
          (+34) 612 738 104
        </li>
        <li>
          <svg class="icon-mail" viewBox="0 0 24 24" aria-hidden="true"><rect x="2.5" y="5" width="19" height="14" rx="1.5"/><path d="M3 6l9 7 9-7"/></svg>
          peter@quorvane.net
        </li>
      </ul>
    </div>
  </section>

  <section class="card card--back" aria-label="Card back">
    <div class="back__watermark" aria-hidden="true">Quorvane</div>
    <div class="back__name">Quorvane Management</div>
  </section>
</main>
</body>
</html>
```